모아큐브는 업무 공간이 필요한 소호 디자이너나 아티스트 등 크리에이터들을 위한 차별화 된 사무 공간/공유 오피스 브랜드입니다.
모아큐브는 최고의 비지니스 입지인 서린역 근처 청운대로변에 위치해 있으며,
360평 면적에 40개의 개인 오피스 (S (2.5평), M (3.5평), L (5-6평) 3종류의 룸으로 구성)와
80석의 Hot desk로 구성되어 있습니다.
저희는 모든 개인 오피스를 기존의 타 브랜드들에 비해 약 20% 가량 넓게 제공함과 동시에 전실 창가로 배치하여 쾌적한 사무 공간을 제공합니다. 또한,
최적화된 조명 시스템과 자연광을 이용할 수 있는 포토 스튜디오,
각종 공구들이 준비된 작업 공간 툴룸,
트렌디하게 제품을 전시할 수 있는 쇼룸,
다양한 소재를 접할 수 있는 Material Library,
예약제로 운영될 미팅룸과 발렛 서비스, 샤워실, 폰 부스 등
크리에이티브 입주사들의 편리와 원활한 작업을 우선시 한 다양한 편의 시설을 제공할 예정입니다.
cctv와 24시간 대응 가능한 비상벨 운영으로 입주자들의 안전에도 세심하게 신경을 썼으며, 편리한 예약과 원활한 소통을 위한 모바일 서비스 또한 기획 중에 있습니다. 그 외 에도 다양하고 도움되는 흥미로운 프로그램들을 개발하여 입주사들의 웰빙과 성장에 동참하고자 합니다.

```html
<!DOCTYPE html>
<html lang="ko">
<head>
<meta charset="utf-8">
<title>MOACUBE Stationery Set</title>
<link rel="stylesheet" href="https://fonts.googleapis.com/css2?family=Open+Sans:wght@400;600;700;800&family=Noto+Sans+KR:wght@400;700&display=swap">
<style>
  :root {
    --bg: #e4e5e7;
    --paper: #f7f7f7;
    --ink: #1f1f1f;
    --ink-soft: #4a4a4a;
    --muted: #8c8c8c;
    --dark: #222222;
    --dark-2: #2c2c2c;
    --accent-band: #2a2a2a;
    --accent-band-soft: #3d3d3d;
    --logo-grey: #8a8a8a;
    --shadow: 0 2px 6px rgba(0,0,0,.12);
  }
  * { box-sizing: border-box; margin: 0; padding: 0; }
  html, body { width: 1200px; height: 1200px; overflow: hidden; }
  body {
    background: var(--bg);
    font-family: "Open Sans", "Noto Sans KR", sans-serif;
    color: var(--ink);
    position: relative;
  }
  .piece { position: absolute; box-shadow: var(--shadow); overflow: hidden; }
  .wordmark { font-family: "Open Sans", sans-serif; font-weight: 800; letter-spacing: .04em; white-space: nowrap; }

  /* Edge band accent */
  .edge-band { position: absolute; right: 0; background: var(--accent-band); }
  .edge-square { position: absolute; background: var(--accent-band); }

  /* Folder */
  .folder { left: 130px; top: 204px; width: 400px; height: 552px; background: var(--dark); }
  .folder .wordmark { position: absolute; left: 0; right: 0; bottom: 30px; text-align: center; color: var(--logo-grey); font-size: 18px; }

  /* Letterhead */
  .letterhead { left: 554px; top: 214px; width: 382px; height: 540px; background: var(--paper); }
  .letterhead .wordmark { position: absolute; left: 20px; top: 20px; font-size: 15px; color: var(--ink-soft); }
  .contact { position: absolute; font-family: "Noto Sans KR", "Open Sans", sans-serif; font-size: 5.5px; line-height: 8.5px; color: var(--ink-soft); white-space: nowrap; }
  .letterhead .contact { left: 20px; top: 42px; }
  .letter-body { position: absolute; left: 30px; top: 100px; width: 220px; font-size: 7.4px; line-height: 11.5px; color: var(--ink); }
  .letter-body .salutation { font-weight: 700; margin-bottom: 12px; }
  .letter-body p { margin-bottom: 12px; }
  .signature { position: absolute; left: 140px; top: 394px; width: 110px; height: 36px; background: linear-gradient(90deg, #d9d9d9, #e9e9e9); }
  .sign-off { position: absolute; left: 30px; top: 416px; font-size: 7.4px; line-height: 11px; }
  .sign-off strong { font-weight: 700; }
  .letter-footer { position: absolute; left: 30px; bottom: 10px; font-size: 5.5px; color: var(--muted); white-space: nowrap; }
  .letterhead .edge-band { bottom: 0; width: 12px; height: 320px; }
  .letterhead .edge-square { right: 20px; bottom: 0; width: 12px; height: 12px; }

  /* Envelope front */
  .envelope-front { left: 80px; top: 790px; width: 384px; height: 190px; background: var(--paper); }
  .envelope-front .wordmark { position: absolute; left: 14px; top: 12px; font-size: 12px; color: var(--ink-soft); }
  .envelope-front .contact { left: 14px; top: 30px; font-size: 4.8px; line-height: 7.5px; }
  .envelope-front .edge-band { top: 0; width: 10px; height: 190px; }
  .envelope-front .edge-square { right: 18px; top: 0; width: 10px; height: 10px; }

  /* Envelope back */
  .envelope-back { left: 494px; top: 790px; width: 380px; height: 190px; background: var(--paper); }
  .envelope-back svg { position: absolute; left: 0; top: 0; }
  .flap-line { position: absolute; left: 0; right: 0; top: 10px; text-align: center; font-size: 5px; color: #cfcfcf; }

  /* Business cards */
  .card { left: 940px; width: 160px; background: var(--dark-2); }
  .card-front { top: 790px; height: 90px; }
  .card-front .wordmark { position: absolute; left: 12px; top: 35px; font-size: 13px; color: #9a9a9a; }
  .card-front .edge-band { top: 0; width: 6px; height: 90px; background: var(--accent-band-soft); }
  .card-back { top: 902px; height: 96px; background: var(--dark); color: #bdbdbd; }
  .card-back .role { position: absolute; left: 12px; top: 10px; font-size: 4.6px; }
  .card-back .name { position: absolute; left: 12px; top: 17px; font-family: "Noto Sans KR", sans-serif; font-size: 6.5px; font-weight: 700; color: #e0e0e0; }
  .card-back .contact { left: 12px; top: 32px; font-size: 4.4px; line-height: 7px; color: #b5b5b5; }
  .card-back .card-name { position: absolute; left: 12px; bottom: 8px; font-size: 4.6px; color: #9a9a9a; letter-spacing: .06em; white-space: nowrap; }
</style>
</head>
<body>

  <section class="piece folder" aria-label="Presentation folder">
    <div class="wordmark">MOACUBE</div>
  </section>

  <article class="piece letterhead" aria-label="Letterhead">
    <div class="wordmark">MOACUBE</div>
    <div class="contact">
      서울시 중구 청운대로 123, 10층<br>
      T. 02. 555. 0148<br>
      E. hello@moacube.kr<br>
      W. www.moacube.kr
    </div>
    <div class="letter-body">
      <p class="salutation">Dear Mr. Owen Harlow</p>
      <p>A letterhead is the heading at the top of a sheet of letter paper (stationery). That heading usually consists of a name and an address, and a logo or corporate design, and sometimes a background pattern. The term "letterhead" is often used to refer to the whole sheet imprinted with such a heading.</p>
      <p>Many companies and individuals prefer to create a letterhead template in a word processor or other software application. This generally includes the same information as pre-printed stationery but without the additional costs involved.</p>
      <p>Letterhead can then be printed on stationery (or plain paper) as needed on a local output device or sent electronically. That heading usually consists of a name and an address, and a logo or corporate design, and sometimes a background pattern. The term "letterhead" is often used to refer to the whole sheet imprinted with such a heading.</p>
      <p>Sincerely,</p>
    </div>
    <div class="signature" role="img" aria-label="Handwritten signature"></div>
    <div class="sign-off"><strong>Rosalind</strong><br>Marketing Director</div>
    <div class="letter-footer">We can work together to make this world more beautiful</div>
    <div class="edge-band" aria-hidden="true"></div>
    <div class="edge-square" aria-hidden="true"></div>
  </article>

  <section class="piece envelope-front" aria-label="Envelope front">
    <div class="wordmark">MOACUBE</div>
    <div class="contact">
      서울시 중구 청운대로 123, 10층<br>
      T. 02. 555. 0148<br>
      E. hello@moacube.kr<br>
      W. www.moacube.kr
    </div>
    <div class="edge-band" aria-hidden="true"></div>
    <div class="edge-square" aria-hidden="true"></div>
  </section>

  <section class="piece envelope-back" aria-label="Envelope back">
    <svg width="380" height="190" viewBox="0 0 380 190" aria-hidden="true">
      <polygon points="0,0 380,0 380,18 340,60 40,60 0,18" fill="var(--dark)"/>
      <polyline points="0,190 190,80 380,190" fill="none" stroke="#dcdcdc" stroke-width="1"/>
    </svg>
    <div class="flap-line">We can work together to make this world more beautiful</div>
  </section>

  <section class="piece card card-front" aria-label="Business card front">
    <div class="wordmark">MOACUBE</div>
    <div class="edge-band" aria-hidden="true"></div>
  </section>

  <section class="piece card card-back" aria-label="Business card back">
    <div class="role">Community Manager</div>
    <div class="name">홍소라</div>
    <div class="contact">
      T. 02. 555. 0148<br>
      M. 010. 2871. 4406<br>
      E. sora@moacube.kr<br>
      서울시 중구 청운대로 123
    </div>
    <div class="card-name">MOACUBE 모아큐브</div>
  </section>

</body>
</html>
```